Looking for updated Letterhead and Compliments Slips to go with our new updated logo. This stationary will be used for letters to suppliers and customers so needs to be practical while also quite classic.

We are an engineering company so needs to be clean and precise

Target Market(s)

SME'S and large automotive customers

Industry/Entity Type

Automotive

Font styles to use
Sans Serif

Colors
85acd3
0356a4
0792cd
33a6d7
85abd2
ffffff

Requirements
Must have
• Address details as below
• KT Fabrications Limited
• Marbury Close
• Hollinsby
• Westmoorshire
• DN47 3XP, UK
• Telephone: +44 (0)1632 960418
• Fax: +44 (0)1632 960735
• Email: sales@ktfabrications.example
• Web: www.ktfabrications.example
Nice to have
• Nice to have some element of being a British Manufacturer

```html
<!DOCTYPE html>
<html lang="en">
<head>
<meta charset="utf-8">
<title>KT Fabrications Stationery</title>
<link href="https://fonts.googleapis.com/css2?family=Montserrat:wght@500&family=Open+Sans:wght@400&family=Yellowtail&display=swap" rel="stylesheet">
<style>
:root{
  --navy:#0356a4;
  --sky:#0792cd;
  --ink:#1f1f1f;
  --swoosh:#231f20;
  --paper:#ffffff;
  --paper-fade:#eeeff1;
  --stage:#e4e4e4;
  --faint:#e7eaef;
}
*{margin:0;padding:0;box-sizing:border-box}
html,body{width:1200px;height:1113px;overflow:hidden;background:var(--stage)}
body{position:relative;font-family:"Open Sans",sans-serif;color:var(--ink)}
.sheet{position:absolute;background:linear-gradient(180deg,var(--paper) 0%,var(--paper) 40%,var(--paper-fade) 100%);overflow:hidden;box-shadow:0 2px 6px rgba(0,0,0,.18)}
.letterhead{top:66px;width:560px;height:723px}
.letterhead--blank{left:48px}
.letterhead--letter{left:622px}
.compliments{left:347px;top:818px;width:543px;height:257px}
.brand{position:absolute;left:24px;top:67px;display:flex;align-items:center;gap:8px;font-family:"Montserrat",sans-serif;font-weight:500;font-size:16px;letter-spacing:4px;color:var(--navy)}
.brand-dot{width:12px;height:12px;border-radius:50%;background:var(--navy)}
.address{position:absolute;left:404px;top:48px;font-size:10.5px;line-height:13px;font-style:normal}
.address .company{color:var(--navy);display:flex;align-items:center;gap:4px;margin-left:-11px}
.address .line{display:block}
.pin{width:8px;height:10px}
.watermark{position:absolute;left:0;right:0;top:330px;text-align:center;font-family:"Montserrat",sans-serif;font-weight:500;font-size:52px;letter-spacing:6px;color:var(--faint)}
.footer{position:absolute;left:0;bottom:0;width:100%;height:90px}
.footer svg{position:absolute;inset:0;width:100%;height:100%}
.contacts{position:absolute;left:0;right:0;bottom:8px;display:flex;justify-content:center;gap:10px;font-size:9px;color:#fff;white-space:nowrap}
.contacts span{display:flex;align-items:center;gap:4px}
.contacts svg{position:static;width:8px;height:8px}
.letter{position:absolute;left:24px;top:140px;width:512px;font-size:9.7px;line-height:16.3px}
.letter .date{margin-bottom:4px}
.letter .recipient{margin-bottom:17px}
.letter .salutation{margin-bottom:11px}
.letter p.body{margin-bottom:19px}
.letter .closing{margin-top:35px}
.signature{font-family:"Yellowtail",cursive;font-size:20px;color:var(--navy);line-height:24px}
.compliments .brand{top:88px;left:23px}
.compliments .address{left:381px;top:59px}
.compliments .footer{height:75px}
.slip-title{position:absolute;left:176px;top:178px;font-family:"Yellowtail",cursive;font-size:28px;color:var(--navy);transform:rotate(-3deg)}
</style>
</head>
<body>

<section class="sheet letterhead letterhead--blank">
  <div class="brand"><span class="brand-dot"></span>KT FABRICATIONS</div>
  <address class="address">
    <span class="company"><svg class="pin" viewBox="0 0 8 10"><path d="M4 0a4 4 0 0 1 4 4c0 3-4 6-4 6S0 7 0 4a4 4 0 0 1 4-4z" fill="#0356a4"/><circle cx="4" cy="4" r="1.5" fill="#fff"/></svg>KT Fabrications Limited</span>
    <span class="line">Marbury Close, Hollinsby</span>
    <span class="line">Westmoorshire, DN47 3XP, UK</span>
  </address>
  <div class="watermark" aria-hidden="true">KT</div>
  <div class="footer">
    <svg viewBox="0 0 560 90" preserveAspectRatio="none">
      <path d="M0 8 C30 28 90 48 220 51 C360 53 480 38 560 40 L560 44 C480 43 360 59 220 59 C100 59 30 53 0 46Z" fill="#231f20"/>
      <path d="M0 50 C80 64 180 66 280 61 C400 55 500 44 560 46 L560 90 L0 90Z" fill="#0356a4"/>
    </svg>
    <div class="contacts">
      <span><svg viewBox="0 0 10 10"><path d="M2 0l2 2-1 2c1 2 2 3 3 3l1-1 2 2-1 2C3 10 0 6 0 2z" fill="#fff"/></svg>+44 (0)1632 960418</span>
      <span><svg viewBox="0 0 10 10"><rect x="1" y="3" width="8" height="6" fill="#fff"/><rect x="3" y="0" width="4" height="3" fill="#fff"/></svg>+44 (0)1632 960735</span>
      <span><svg viewBox="0 0 10 10"><rect x="0" y="2" width="10" height="7" fill="#fff"/><path d="M0 2l5 4 5-4" stroke="#0356a4" fill="none"/></svg>sales@ktfabrications.example</span>
      <span><svg viewBox="0 0 10 10"><circle cx="5" cy="5" r="4.3" fill="none" stroke="#fff"/><path d="M1 5h8M5 1v8" stroke="#fff"/></svg>www.ktfabrications.example</span>
    </div>
  </div>
</section>

<section class="sheet letterhead letterhead--letter">
  <div class="brand"><span class="brand-dot"></span>KT FABRICATIONS</div>
  <address class="address">
    <span class="company"><svg class="pin" viewBox="0 0 8 10"><path d="M4 0a4 4 0 0 1 4 4c0 3-4 6-4 6S0 7 0 4a4 4 0 0 1 4-4z" fill="#0356a4"/><circle cx="4" cy="4" r="1.5" fill="#fff"/></svg>KT Fabrications Limited</span>
    <span class="line">Marbury Close, Hollinsby</span>
    <span class="line">Westmoorshire, DN47 3XP, UK</span>
  </address>
  <div class="letter">
    <p class="date">May 05, 2017</p>
    <p class="recipient">Your Name<br>Title</p>
    <p class="salutation">Dear Mr. Lorem,</p>
    <p class="body">Lorem ipsum dolor sit amet, consectetuer adipiscing elit, sed diam nonummy nibh euismod tincidunt ut laoreet dolore magna aliquam erat volutpat. Ut wisi enim ad minim veniam, quis nostrud exerci tation ullamcorper suscipit lobortis nisl ut aliquip ex ea commodo consequat. Duis autem vel eum iriure dolor in hendrerit in vulputate velit esse molestie consequat, vel illum dolore eu feugiat nulla facilisis at vero eros et accumsan et iusto odio dignissim qui blandit praesent luptatum zzril delenit augue duis dolore te feugait nulla facilisi.</p>
    <p class="body">Lorem ipsum dolor sit amet, consectetuer adipiscing elit, sed diam nonummy nibh euismod tincidunt ut laoreet dolore magna aliquam erat volutpat. Ut wisi enim ad minim veniam, quis nostrud exerci tation ullamcorper suscipit lobortis nisl ut aliquip ex ea commodo consequat. Duis autem vel eum iriure dolor in hendrerit in vulputate velit esse molestie consequat, vel illum dolore eu feugiat nulla facilisis at vero eros et accumsan et iusto odio dignissim qui blandit praesent luptatum zzril delenit augue duis dolore te feugait nulla facilisi.</p>
    <p class="body">Lorem ipsum dolor sit amet, consectetuer adipiscing elit, sed diam nonummy nibh euismod tincidunt ut laoreet dolore magna aliquam erat volutpat. Ut wisi enim ad minim veniam, quis nostrud exerci tation ullamcorper suscipit lobortis nisl ut aliquip ex ea commodo consequat. Duis autem vel eum iriure dolor in hendrerit in vulputate velit esse molestie consequat, vel illum dolore eu feugiat nulla facilisis at vero eros et accumsan et iusto odio dignissim qui blandit praesent luptatum zzril delenit augue duis dolore te feugait nulla facilisi.</p>
    <p class="closing">Sincerely Your,</p>
    <p class="signature">Your Name</p>
  </div>
  <div class="footer">
    <svg viewBox="0 0 560 90" preserveAspectRatio="none">
      <path d="M0 8 C30 28 90 48 220 51 C360 53 480 38 560 40 L560 44 C480 43 360 59 220 59 C100 59 30 53 0 46Z" fill="#231f20"/>
      <path d="M0 50 C80 64 180 66 280 61 C400 55 500 44 560 46 L560 90 L0 90Z" fill="#0356a4"/>
    </svg>
    <div class="contacts">
      <span><svg viewBox="0 0 10 10"><path d="M2 0l2 2-1 2c1 2 2 3 3 3l1-1 2 2-1 2C3 10 0 6 0 2z" fill="#fff"/></svg>+44 (0)1632 960418</span>
      <span><svg viewBox="0 0 10 10"><rect x="1" y="3" width="8" height="6" fill="#fff"/><rect x="3" y="0" width="4" height="3" fill="#fff"/></svg>+44 (0)1632 960735</span>
      <span><svg viewBox="0 0 10 10"><rect x="0" y="2" width="10" height="7" fill="#fff"/><path d="M0 2l5 4 5-4" stroke="#0356a4" fill="none"/></svg>sales@ktfabrications.example</span>
      <span><svg viewBox="0 0 10 10"><circle cx="5" cy="5" r="4.3" fill="none" stroke="#fff"/><path d="M1 5h8M5 1v8" stroke="#fff"/></svg>www.ktfabrications.example</span>
    </div>
  </div>
</section>

<section class="sheet compliments">
  <div class="brand"><span class="brand-dot"></span>KT FABRICATIONS</div>
  <address class="address">
    <span class="company"><svg class="pin" viewBox="0 0 8 10"><path d="M4 0a4 4 0 0 1 4 4c0 3-4 6-4 6S0 7 0 4a4 4 0 0 1 4-4z" fill="#0356a4"/><circle cx="4" cy="4" r="1.5" fill="#fff"/></svg>KT Fabrications Limited</span>
    <span class="line">Marbury Close, Hollinsby</span>
    <span class="line">Westmoorshire, DN47 3XP, UK</span>
  </address>
  <div class="slip-title">With compliments</div>
  <div class="footer">
    <svg viewBox="0 0 560 90" preserveAspectRatio="none">
      <path d="M0 8 C30 28 90 48 220 51 C360 53 480 38 560 40 L560 44 C480 43 360 59 220 59 C100 59 30 53 0 46Z" fill="#231f20"/>
      <path d="M0 50 C80 64 180 66 280 61 C400 55 500 44 560 46 L560 90 L0 90Z" fill="#0356a4"/>
    </svg>
    <div class="contacts">
      <span><svg viewBox="0 0 10 10"><path d="M2 0l2 2-1 2c1 2 2 3 3 3l1-1 2 2-1 2C3 10 0 6 0 2z" fill="#fff"/></svg>+44 (0)1632 960418</span>
      <span><svg viewBox="0 0 10 10"><rect x="1" y="3" width="8" height="6" fill="#fff"/><rect x="3" y="0" width="4" height="3" fill="#fff"/></svg>+44 (0)1632 960735</span>
      <span><svg viewBox="0 0 10 10"><rect x="0" y="2" width="10" height="7" fill="#fff"/><path d="M0 2l5 4 5-4" stroke="#0356a4" fill="none"/></svg>sales@ktfabrications.example</span>
      <span><svg viewBox="0 0 10 10"><circle cx="5" cy="5" r="4.3" fill="none" stroke="#fff"/><path d="M1 5h8M5 1v8" stroke="#fff"/></svg>www.ktfabrications.example</span>
    </div>
  </div>
</section>

</body>
</html>
```